Salon website

Need a web design for a new blow dry and hair extension boutique in CT
would like the color scheme to be gray, white and tiffany blue
Create a web site with about 4 pages showing
1 about us page
1 blow dry services page
1 hair extension services page
1 contact us page
1 membership page
1 parties page

Industry/Entity Type

Boutique

Colors
86cfc6
cfeae6
33b7a4
aaaaaa
cbcbcb
ffffff

```html
<!DOCTYPE html>
<html lang="en">
<head>
<meta charset="utf-8">
<title>Velvet Strand — Blow Dry &amp; Hair Extension Boutique</title>
<link rel="stylesheet" href="https://fonts.googleapis.com/css2?family=Old+Standard+TT:wght@400;700&display=swap">
<style>
  :root {
    --teal: #3ec9c4;
    --teal-dark: #33b7a4;
    --teal-pale: #cfeae6;
    --grey: #aaaaaa;
    --grey-light: #cbcbcb;
    --grey-line: #dedede;
    --text: #555555;
    --text-dark: #3a3a3a;
    --page: #f6f6f6;
    --white: #ffffff;
  }
  * { box-sizing: border-box; margin: 0; padding: 0; }
  html, body { width: 809px; height: 1200px; overflow: hidden; }
  body {
    position: relative;
    background: var(--page);
    font-family: "Old Standard TT", Georgia, serif;
    color: var(--text);
  }
  .abs { position: absolute; }

  /* header */
  .brand { left: 0; width: 809px; top: 18px; text-align: center; }
  .brand-mark { width: 92px; height: 92px; border-radius: 50%; border: 4px solid var(--teal); margin: 0 auto; }
  .brand-name { margin-top: 14px; font-size: 31px; color: var(--teal); font-weight: 700; letter-spacing: .5px; }

  .nav {
    left: 0; top: 197px; width: 809px; height: 66px;
    border-top: 1px solid var(--grey-line); border-bottom: 1px solid var(--grey-line);
    background: var(--page);
  }
  .nav-sep { position: absolute; top: 0; width: 1px; height: 64px; background: var(--grey-line); }
  .nav-item { position: absolute; top: 24px; font-size: 12px; color: #8a8a8a; transform: translateX(-50%); white-space: nowrap; }

  /* hero */
  .teal-band { left: 0; top: 511px; width: 809px; height: 273px; background: var(--teal); }
  .slider-shadow {
    left: 150px; top: 530px; width: 509px; height: 30px;
    background: radial-gradient(ellipse at center top, rgba(0,0,0,.28), rgba(0,0,0,0) 70%);
  }
  .slide {
    left: 116px; top: 267px; width: 577px; height: 244px;
    background: linear-gradient(100deg, #d9dcdf 0%, #c9cbcd 22%, #b98a6c 48%, #6d4330 75%, #c6c8cb 100%);
  }
  .slider-bar { left: 116px; top: 511px; width: 577px; height: 32px; background: var(--white); }
  .dots { left: 0; width: 577px; top: 10px; display: flex; justify-content: center; gap: 6px; }
  .dot { width: 13px; height: 13px; border-radius: 50%; background: #bdbdbd; border: 1px solid #9d9d9d; }
  .dot.active { background: var(--teal); border-color: var(--teal-dark); }

  .welcome-title { left: 0; width: 809px; top: 590px; text-align: center; color: var(--white); font-size: 26px; letter-spacing: .5px; }
  .welcome-rule { left: 191px; top: 625px; width: 426px; height: 1px; background: rgba(255,255,255,.85); }
  .welcome-text { left: 160px; width: 489px; top: 645px; text-align: center; color: var(--white); font-size: 11.5px; line-height: 14px; font-weight: 700; }
  .btn-read {
    left: 365px; top: 721px; width: 87px; height: 34px;
    border: 1px solid rgba(255,255,255,.9); color: var(--white);
    font-size: 10px; font-weight: 700; display: flex; align-items: center; justify-content: center;
  }

  /* columns */
  .col-title { top: 803px; font-size: 19px; color: var(--teal); letter-spacing: .3px; }
  .col-rule { top: 830px; height: 1px; background: var(--grey-light); }
  .col-rule::after { content: ""; position: absolute; left: 25%; width: 50%; top: -1px; height: 2px; background: var(--teal); }

  .popular { left: 116px; top: 843px; width: 157px; list-style: none; }
  .popular li {
    height: 27px; line-height: 27px; padding-left: 15px; font-size: 11px; color: #8c8c8c;
    border-bottom: 1px solid var(--grey-line); position: relative;
  }
  .popular li::before { content: ""; position: absolute; left: 3px; top: 12px; width: 4px; height: 4px; border-radius: 50%; background: #9a9a9a; }
  .popular li.active { color: var(--teal); }
  .popular li.active::before { background: var(--teal); }
  .popular li:last-child { border-bottom: none; }

  .trend-photo { left: 312px; top: 848px; width: 188px; height: 93px; background: linear-gradient(90deg, #2e2a26 0%, #8a7150 40%, #e2c992 60%, #3a352f 100%); }
  .trend-text { left: 312px; top: 950px; width: 188px; font-size: 10px; line-height: 12px; color: #8a8a8a; }
  .trend-more { left: 312px; top: 988px; font-size: 10px; color: var(--teal); font-weight: 700; }

  .service { left: 533px; width: 160px; }
  .service-title { font-size: 10.5px; color: var(--teal); font-weight: 700; padding-left: 16px; position: relative; }
  .service-title::before { content: ""; position: absolute; left: 2px; top: 5px; width: 4px; height: 4px; border-radius: 50%; background: var(--teal); }
  .service-text { margin-top: 3px; padding-left: 16px; font-size: 9.5px; line-height: 11.5px; color: #a5a5a5; }
  .service-rule { left: 533px; top: 907px; width: 160px; height: 1px; background: var(--grey-line); }

  /* feature boxes */
  .features { left: 116px; top: 1020px; width: 577px; height: 91px; border: 1px solid var(--grey-line); display: flex; }
  .feature { flex: 1; text-align: center; border-right: 1px solid var(--grey-line); padding-top: 12px; }
  .feature:last-child { border-right: none; }
  .feature-title { font-size: 15px; color: var(--text-dark); letter-spacing: .5px; }
  .feature-more { margin-top: 3px; font-size: 8.5px; color: var(--text-dark); font-weight: 700; letter-spacing: .5px; }
  .feature-arrow { margin: 9px auto 0; width: 17px; height: 17px; border-radius: 50%; border: 1px solid var(--grey-line); display: flex; align-items: center; justify-content: center; }
  .social { margin-top: 6px; display: flex; justify-content: center; gap: 5px; }
  .social span { width: 20px; height: 20px; border-radius: 50%; background: var(--grey-light); }

  /* footer */
  .footer {
    left: 0; top: 1155px; width: 809px; height: 45px; background: var(--teal);
    display: flex; align-items: center; justify-content: center;
    color: var(--white); font-size: 10px; font-weight: 700; letter-spacing: .4px;
  }
</style>
</head>
<body>

<header>
  <div class="abs brand">
    <div class="brand-mark"></div>
    <div class="brand-name">Velvet Strand</div>
  </div>
  <nav class="abs nav">
    <span class="nav-sep" style="left:227px"></span>
    <span class="nav-sep" style="left:383px"></span>
    <span class="nav-sep" style="left:571px"></span>
    <span class="nav-item" style="left:170px">About Us</span>
    <span class="nav-item" style="left:305px">Blow Dry Services</span>
    <span class="nav-item" style="left:477px">Hair Extension Services</span>
    <span class="nav-item" style="left:636px">Contact Us</span>
  </nav>
</header>

<section class="hero">
  <div class="abs teal-band"></div>
  <div class="abs slider-shadow"></div>
  <div class="abs slide" role="img" aria-label="Photo of a smiling woman with long brown hair being blow dried"></div>
  <div class="abs slider-bar">
    <div class="abs dots">
      <span class="dot"></span><span class="dot active"></span><span class="dot"></span><span class="dot"></span>
    </div>
  </div>
  <h1 class="abs welcome-title" style="font-weight:400">WELCOME HAIR DRY</h1>
  <div class="abs welcome-rule"></div>
  <p class="abs welcome-text">Lorem ipsum dolor sit amet, consectetuer adipiscing elit, sed diam nonummy nibh euismod tincidunt ut laoreet dolore magna aliquam erat volutpat. Ut wisi enim ad minim veniam, quis nostrud exerci tation ullamcorper suscipit lobortis nisl ut aliquip ex ea commodo consequat.</p>
  <a class="abs btn-read">Read More</a>
</section>

<section class="columns">
  <h2 class="abs col-title" style="left:116px;font-weight:400">MOST POPULAR</h2>
  <div class="abs col-rule" style="left:116px;width:157px"></div>
  <ul class="abs popular">
    <li class="active">Hair Coloring</li>
    <li>Henna Body Art</li>
    <li>Manicures</li>
    <li>Pedicures</li>
    <li>Waxing</li>
    <li>Skin Care</li>
  </ul>

  <h2 class="abs col-title" style="left:312px;font-weight:400">HAIR TRENDS</h2>
  <div class="abs col-rule" style="left:312px;width:160px"></div>
  <div class="abs trend-photo" role="img" aria-label="Photo of a woman with voluminous blonde curls"></div>
  <p class="abs trend-text">Lorem ipsum dolor sit amet, consectetuer adipiscing elit, sed diam nonummy nibh euismod tincidunt ut laoreet dolore.</p>
  <a class="abs trend-more">Read More &gt;&gt;</a>

  <h2 class="abs col-title" style="left:533px;font-weight:400">OUR SERVICES</h2>
  <div class="abs col-rule" style="left:533px;width:160px"></div>
  <div class="abs service" style="top:847px">
    <div class="service-title">Creative Hair Cuts</div>
    <p class="service-text">Soft layered cuts shaped to suit your face and style.</p>
  </div>
  <div class="abs service-rule"></div>
  <div class="abs service" style="top:920px">
    <div class="service-title">Permanent Make Up</div>
    <p class="service-text">Natural makeup for events, photos and special evenings out.</p>
  </div>
</section>

<section class="abs features">
  <div class="feature">
    <div class="feature-title">TESTIMONIALS</div>
    <div class="feature-more">READ MORE</div>
    <div class="feature-arrow"><svg width="6" height="8" viewBox="0 0 6 8"><path d="M1.5 1 L4.5 4 L1.5 7" fill="none" stroke="#aaaaaa" stroke-width="1"/></svg></div>
  </div>
  <div class="feature">
    <div class="feature-title">PHOTO &amp; VIDEO</div>
    <div class="feature-more">READ MORE</div>
    <div class="feature-arrow"><svg width="6" height="8" viewBox="0 0 6 8"><path d="M1.5 1 L4.5 4 L1.5 7" fill="none" stroke="#aaaaaa" stroke-width="1"/></svg></div>
  </div>
  <div class="feature">
    <div class="feature-title">FOLLOW US</div>
    <div class="feature-more">READ MORE</div>
    <div class="social"><span></span><span></span><span></span><span></span></div>
  </div>
</section>

<footer class="abs footer">© 2014 VELVET STRAND &nbsp;ALL RESERVED</footer>

</body>
</html>
```